Non-profit Needs PP Template, Flyer and Banner Ad to Educate Addiction Counselors

We need a PowerPoint Template design, flyer to advertise a large amount of text (that matches the PowerPoint design), and Banner Ad (that matches the other two products) for a non-profit organization based in Washington, DC called "KELMOS, The Halvern Counseling Fellowship". KELMOS, the Halvern Counseling Fellowship, represents the professional interests of more than 75,000 addiction counselors, educators and other addiction-focused health care professionals in the United States, Canada and abroad. KELMOS’s members are addiction counselors, educators and other addiction-focused health care professionals, who specialize in addiction prevention, treatment, recovery support and education. An important part of the healthcare continuum, KELMOS members and its 44 state affiliates work to create healthier individuals, families and communities through prevention, intervention, quality treatment and recovery support.

As a part of the federal government’s efforts to promote recovery for all Americans affected by mental illness and/or addiction, in May 2009, the United States government announced its "Steadfast Harbor (SHB) Initiative." The SHB Initiative is designed to hasten awareness, acceptance, and adoption of recovery-based practices in the delivery of addiction-related services and builds on QORTEL’s definition and fundamental components of recovery.

The purpose of the 3 pieces is to educate thousands of therapists about "Recovery Concepts". The design needs to reflect the following definition and dimensions:

Recovery means: A process of change through which individuals improve their health and wellness, live a self-directed life, and strive to reach their full potential.

Four major dimensions that support a life in recovery:
• Health: overcoming or managing one’s disease(s) as well as living in a physically and emotionally healthy way;
• Home: a stable and safe place to live;
• Purpose: meaningful daily activities, such as a job, school, volunteerism, family caretaking, or creative endeavors, and the independence, income and resources to participate in society; and
• Community: relationships and social networks that provide support, friendship, love and hope.

Our logo is attached. No branding exists for the Steadfast Harbor Initiative. I envision some original artwork or image used throughout each piece, with the same colors, fonts, etc. so it looks like the same thing just in different formats - branding.

The final PP design must be suitable for both online display and face-to-face projector display. Need title page and 3 different transition slides. Files must be easily editable.

The flyer is to advertise the 9 webinars of the project. Text for the flyer is here: http://www.kelmos-example.org/education/pathways/shb-webinars

The last component is a matching Banner Ad that can go at the top of our website that advertises the project: www.kelmos-example.org. Let me know if you more specifics on size or something else that I am not aware of.

Again, all of these three components must match each other, with the overall message being "Steadfast Harbor (SHB) Initiative" - not our organization "KELMOS".

Other projects we have accepted from Drawvantry contest previously are attached and here (DO NOT USE THESE FOR THIS ORIGINAL DESIGN CONTEST - only for reference about our tastes):
http://www.kelmos-example.org/images/kelmos%20webinar%20flyer.pdf
http://www.kelmos-example.org/images/trainingflyer.pdf

Open to designs with any colors, and our company color is royal blue.

Please note:

The focus of this project is NOT the organization "KELMOS", but the project "Steadfast Harbor (SHB) Initiative".  We are looking for a complete branding package for this project that has its own colors, logo/graphics, look, and feel, so the banner ad, advertisement flyer, and PowerPoint slides all match and look the same.  

Please DO NOT use any images or designs from previously developed flyers.  We are looking for something original.  I only included these in the brief so you could see other items we have developed for other purposes and to get an idea of what we like.  

Thank you - 
Bryn

Reason: I have modified the information in the brief to be more clear. This extension will allow designers time to prepare submissions for each of the three components. Thanks to all of you! Bryn

Hello everyone - 

I just learned that the specs for the banner ad should be 660x150. A jpg format works best.
Thanks for all of your submissions!
Bryn

Target Market(s)

Adult professionals, diverse in culture and age

Industry/Entity Type

Non-Profit

Requirements
Must have
• The Title of the Entire program is "Steadfast Harbor (SHB) Initiative"
KELMOS, the Halvern Counseling Fellowship is the organization that is creating the program
Logo must be on the flyer and the Title page of the PP template
Nice to have
• Individuals who have personally experienced substance abuse either with themselves or family members are encouraged to make submissions.

```html
<!DOCTYPE html>
<html lang="en">
<head>
<meta charset="utf-8">
<title>Steadfast Harbor (SHB) Webinars</title>
<link href="https://fonts.googleapis.com/css2?family=Source+Sans+3:wght@400;600&display=swap" rel="stylesheet">
<style>
  :root {
    --sea-deep: #2f7f84;
    --sea-mid: #4f9c9d;
    --sea-light: #8cc3bf;
    --white: #ffffff;
    --ribbon: rgba(190, 205, 225, 0.55);
    --mark-ink: #2f3f6e;
    --pill: #b9c9e0;
    --dot: rgba(255, 255, 255, 0.85);
  }
  * { margin: 0; padding: 0; box-sizing: border-box; }
  html, body { width: 1200px; height: 900px; overflow: hidden; }
  body { font-family: "Source Sans 3", "Myriad Pro", sans-serif; color: var(--white); }
  .slide { position: relative; width: 1200px; height: 900px; overflow: hidden; }
  .backdrop {
    position: absolute; inset: 0;
    background:
      radial-gradient(ellipse 700px 320px at 560px 250px, rgba(220,240,236,0.45), transparent 70%),
      radial-gradient(ellipse 500px 300px at 900px 700px, rgba(200,230,226,0.25), transparent 70%),
      linear-gradient(160deg, var(--sea-mid) 0%, var(--sea-deep) 55%, var(--sea-mid) 100%);
  }
  .lighthouse-area {
    position: absolute; left: 80px; top: 280px; width: 200px; height: 620px;
    background: linear-gradient(180deg, rgba(230,245,242,0.55), rgba(200,228,224,0.35));
  }
  .social { position: absolute; top: 29px; left: 70px; display: flex; gap: 32px; }
  .social span { width: 48px; height: 48px; border-radius: 50%; background: var(--dot); }
  .rule-top { position: absolute; left: 40px; top: 91px; width: 265px; height: 2px; background: var(--white); }
  .org-name {
    position: absolute; left: 40px; top: 104px; width: 265px;
    text-align: center; font-size: 25px; line-height: 32px; font-weight: 400;
  }
  .ribbon { position: absolute; left: 1020px; top: 0; width: 113px; height: 228px; }
  .ribbon-mark {
    position: absolute; left: 1047px; top: 28px; width: 70px; height: 70px;
    border: 2px solid var(--mark-ink); background: rgba(255,255,255,0.15);
  }
  .ribbon-name {
    position: absolute; left: 1020px; top: 116px; width: 113px;
    text-align: center; font-size: 19px; font-weight: 600; color: var(--white);
  }
  .title {
    position: absolute; left: 320px; top: 306px;
    font-size: 47px; line-height: 60px; font-weight: 400;
  }
  .title-rule { position: absolute; left: 320px; top: 434px; width: 660px; height: 2px; background: var(--pill); }
  .title-pill { position: absolute; left: 965px; top: 420px; width: 174px; height: 30px; border-radius: 15px; background: var(--pill); }
  .dimensions {
    position: absolute; left: 320px; width: 660px; top: 866px;
    text-align: center; font-size: 20px; letter-spacing: 4px; font-weight: 400;
  }
</style>
</head>
<body>
<main class="slide">
  <div class="backdrop" role="img" aria-label="Teal sky with soft clouds under a fine crosshatch texture"></div>
  <div class="lighthouse-area" role="img" aria-label="Tall white lighthouse tower rising from the lower left"></div>

  <nav class="social" aria-label="Social links"><span></span><span></span><span></span></nav>
  <div class="rule-top"></div>
  <p class="org-name">The Halvern Counseling<br>Fellowship</p>

  <svg class="ribbon" viewBox="0 0 113 228" aria-hidden="true">
    <polygon points="0,0 113,0 113,228 0,160" fill="var(--ribbon)"/>
  </svg>
  <div class="ribbon-mark"></div>
  <p class="ribbon-name">KELMOS</p>

  <h1 class="title">Steadfast Harbor<br>(SHB) Webinars</h1>
  <div class="title-rule"></div>
  <div class="title-pill"></div>

  <p class="dimensions">Health | Home | Purpose | Community</p>
</main>
</body>
</html>
```